Business Card Design

Vintage looking Hair Salon, where the customer service is 100%. We are based in a cottage. With shabby chic console tables and beautiful ornate mirrors..and rich brown leather cutting chairs. Chandeliers at the window, and a ornate patchwork sofa.
our clientele are 28years upwards.. Mums with small children.. Ladies that lunch, and men that want more than a barbers and are prepared to pay for our services.
I am looking for a classy business card.. That look expensive.. Where our initials WHP become a visual reference.. I was thinking of cream card initials in black on a embossed tarnished silver.. But I'm open to suggestion. I want,  need the design to be able to work with flyers price list ect.

Willowmere Hair Parlour
27 Fenwick Row
Ardley Green
bN42 6TW
FB thewillowmerehairparlour
Info@thewillowmerhairparlour.co.uk
0208 715 2964

```html
<!DOCTYPE html>
<html lang="en">
<head>
<meta charset="utf-8">
<title>Willowmere Hair Parlour – Business Card</title>
<link href="https://fonts.googleapis.com/css2?family=Open+Sans:wght@400;600;700&display=swap" rel="stylesheet">
<style>
  :root {
    --backdrop: #d9dcdf;
    --card: #f4f4f2;
    --ink: #2e2e2e;
    --ink-soft: #4a4a4a;
    --rule: #3a3a3a;
  }
  html, body {
    margin: 0;
    padding: 0;
    width: 1200px;
    height: 675px;
    overflow: hidden;
    background: var(--backdrop);
    font-family: "Open Sans", Arial, sans-serif;
    color: var(--ink);
  }
  .business-card {
    position: absolute;
    left: 130px;
    top: 77px;
    width: 940px;
    height: 521px;
    background: var(--card);
    box-shadow: 0 8px 24px rgba(0,0,0,0.12);
  }
  .brand {
    position: absolute;
    left: 70px;
    top: 0;
    width: 340px;
    height: 100%;
    display: flex;
    flex-direction: column;
    align-items: center;
    justify-content: center;
    gap: 22px;
  }
  .brand-dot {
    width: 26px;
    height: 26px;
    border-radius: 50%;
    background: var(--ink);
  }
  .brand-name {
    font-weight: 700;
    font-size: 34px;
    line-height: 1.2;
    text-align: center;
    text-transform: uppercase;
    letter-spacing: 1px;
    color: var(--ink);
  }
  .divider {
    position: absolute;
    left: 470px;
    top: 120px;
    width: 2px;
    height: 280px;
    background: var(--rule);
  }
  .contact {
    position: absolute;
    left: 530px;
    top: 130px;
    width: 390px;
  }
  .person-name {
    font-weight: 700;
    font-size: 36px;
    margin: 0;
    line-height: 1.1;
  }
  .person-role {
    font-size: 20px;
    color: var(--ink-soft);
    margin: 2px 0 26px 20px;
  }
  .contact-list {
    list-style: none;
    margin: 0;
    padding: 0 0 0 20px;
  }
  .contact-item {
    display: flex;
    align-items: flex-start;
    gap: 16px;
    font-size: 17px;
    line-height: 1.3;
    margin-bottom: 12px;
    color: var(--ink);
  }
  .contact-icon {
    width: 20px;
    height: 20px;
    flex: none;
    fill: var(--ink);
    margin-top: 1px;
  }
  .address {
    font-weight: 600;
  }
</style>
</head>
<body>
  <section class="business-card">
    <div class="brand">
      <span class="brand-dot"></span>
      <div class="brand-name">Willowmere<br>Hair Parlour</div>
    </div>

    <div class="divider"></div>

    <div class="contact">
      <h1 class="person-name">Your Name</h1>
      <div class="person-role">Manager</div>
      <ul class="contact-list">
        <li class="contact-item">
          <svg class="contact-icon" viewBox="0 0 24 24" aria-hidden="true"><path d="M6.6 10.8a15.1 15.1 0 0 0 6.6 6.6l2.2-2.2c.3-.3.7-.4 1-.2 1.1.4 2.3.6 3.6.6.6 0 1 .4 1 1V20c0 .6-.4 1-1 1A17 17 0 0 1 3 4c0-.6.4-1 1-1h3.5c.6 0 1 .4 1 1 0 1.3.2 2.5.6 3.6.1.3 0 .7-.2 1z"/></svg>
          <span>+44 0208 715 2964</span>
        </li>
        <li class="contact-item">
          <svg class="contact-icon" viewBox="0 0 24 24" aria-hidden="true"><path d="M2 5h20v14H2z M3.5 6.5 12 13l8.5-6.5" fill="none" stroke="currentColor" stroke-width="0"/><path d="M2 5h20v2l-10 7L2 7z M2 9l10 7 10-7v10H2z"/></svg>
          <span>Info@thewillowmerhairparlour.co.uk</span>
        </li>
        <li class="contact-item">
          <svg class="contact-icon" viewBox="0 0 24 24" aria-hidden="true"><g fill="none" stroke="#2e2e2e" stroke-width="1.6"><circle cx="12" cy="12" r="9"/><ellipse cx="12" cy="12" rx="4" ry="9"/><path d="M3 12h18M5 7h14M5 17h14"/></g></svg>
          <span>www.thewillowmerehairparlour.co.uk</span>
        </li>
        <li class="contact-item address">
          <svg class="contact-icon" viewBox="0 0 24 24" aria-hidden="true"><path d="M12 2a7 7 0 0 0-7 7c0 5.2 7 13 7 13s7-7.8 7-13a7 7 0 0 0-7-7zm0 9.5A2.5 2.5 0 1 1 12 6.5a2.5 2.5 0 0 1 0 5z"/></svg>
          <span>27 Fenwick Row Ardley Green<br>bN42 6TW FB</span>
        </li>
      </ul>
    </div>
  </section>
</body>
</html>
```